Business Card design which attached logo. Company is called Tailored Shield and main colours are Orange & Black.

Company specialises in Paint Protection and Detailing for supercars.

Details needed on business card:

Sales

Address: Unit 14, 227 Harlow Street, Fernmere Vale, NSW 2391

Phone: 02 8419 2753

website: www.tailoredshield.com.au

Email: sales@tailoredshield.com.au

```html
<!DOCTYPE html>
<html lang="en">
<head>
<meta charset="utf-8">
<title>Tailored Shield – Business Card</title>
<link rel="stylesheet" href="https://fonts.googleapis.com/css2?family=Arimo:wght@400&display=swap">
<style>
  :root {
    --backdrop: #8e8e8e;
    --card: #2a2a2a;
    --orange: #d8521f;
    --ink: #dcdcdc;
  }
  * { margin: 0; padding: 0; box-sizing: border-box; }
  html, body {
    width: 1200px;
    height: 781px;
    overflow: hidden;
    background: var(--backdrop);
    font-family: "Arimo", Arial, sans-serif;
  }
  .card {
    position: absolute;
    left: 350px;
    width: 526px;
    height: 292px;
    background: var(--card);
  }
  .card--front { top: 65px; }
  .card--back  { top: 409px; }

  .holder {
    position: absolute;
    left: 47px;
    top: 47px;
    font-size: 11.5px;
    line-height: 14.5px;
    text-transform: uppercase;
  }
  .holder__name  { color: var(--orange); }
  .holder__title { color: var(--ink); }

  .wordmark {
    color: var(--orange);
    font-weight: 400;
    text-transform: uppercase;
    white-space: nowrap;
    letter-spacing: 0.5px;
  }
  .card--front .wordmark {
    position: absolute;
    right: 46px;
    top: 120px;
    font-size: 21px;
  }
  .card--back .wordmark {
    position: absolute;
    left: 0;
    right: 0;
    top: 189px;
    text-align: center;
    font-size: 22px;
  }

  .contact, .address {
    position: absolute;
    bottom: 38px;
    color: var(--ink);
    font-size: 11.5px;
    line-height: 14.8px;
    text-transform: uppercase;
  }
  .contact { left: 47px; }
  .address { right: 46px; text-align: right; }
</style>
</head>
<body>
  <section class="card card--front">
    <div class="holder">
      <p class="holder__name">Jordan Malvey</p>
      <p class="holder__title">General Manager</p>
    </div>
    <p class="wordmark">Tailored Shield</p>
    <div class="contact">
      <p>02 8419 2753</p>
      <p>sales@tailoredshield.com.au</p>
      <p>www.tailoredshield.com.au</p>
    </div>
    <div class="address">
      <p>Unit 14, 227 Harlow Street</p>
      <p>Fernmere Vale, NSW 2391</p>
    </div>
  </section>

  <section class="card card--back">
    <p class="wordmark">Tailored Shield</p>
  </section>
</body>
</html>
```